Book Cover for a technology book - The Silent Lattice

We are writing a book that is a handbook how to build a hybrid cloud - this is a technology concept where companies use cloud services both from the like of Vornix or Plenquor and also cloud services built in there own data centers - hence the term hybrid cloud. We want a book cover with the title - The Silent Lattice; which signifies that we will be teaching companies how to build a hybrid cloud that just works. We want the tagline - handbook for building Hybrid Clouds. The authors are Corwin Haddle and Ross Pelley. The cover is to be engaging and feel different than your usual technical manual. I don't have any graphics to help out however will be able to refine and tell you what I don and don't like based on your drafts. The book dimensions are yet to be determined, in the first instance it will be a PDF

Target Market(s)

technology executives and specialists

Industry/Entity Type

Information Technology

Colors

Designer to choose colors to be used in the design.

Requirements
Nice to have
• While I don't have a particular view to how it will look, I'd like the style to be more casual than ultra formal

```html
<!DOCTYPE html>
<html lang="en">
<head>
<meta charset="utf-8">
<title>The Silent Lattice — Book Cover</title>
<link href="https://fonts.googleapis.com/css2?family=Montserrat:wght@400;700;800&family=Questrial&display=swap" rel="stylesheet">
<style>
  :root {
    --stage: #e4e4e4;
    --paper: #ffffff;
    --sky: #1b93c4;
    --sky-deep: #0d6e9b;
    --sun: #f6a623;
    --ink: #333333;
    --bar: #232323;
    --title-light: #ffffff;
  }
  html, body {
    margin: 0;
    padding: 0;
    width: 1200px;
    height: 1200px;
    overflow: hidden;
    background: var(--stage);
  }
  .canvas {
    width: 1200px;
    height: 1200px;
    display: flex;
    align-items: center;
    justify-content: center;
  }
  .book-cover {
    width: 846px;
    height: 1116px;
    display: block;
    box-shadow: 0 10px 30px rgba(0,0,0,0.18);
  }
  .author-name {
    font-family: "Questrial", sans-serif;
    font-size: 17px;
    fill: var(--ink);
    letter-spacing: 0.5px;
  }
  .title-lead {
    font-family: "Montserrat", sans-serif;
    font-weight: 800;
    font-size: 36px;
    fill: var(--ink);
  }
  .title-main {
    font-family: "Montserrat", sans-serif;
    font-weight: 800;
    font-size: 74px;
    fill: var(--title-light);
  }
  .tagline {
    font-family: "Montserrat", sans-serif;
    font-weight: 700;
    font-size: 15px;
    fill: var(--ink);
  }
</style>
</head>
<body>
<main class="canvas">
  <svg class="book-cover" viewBox="0 0 423 558" xmlns="http://www.w3.org/2000/svg" aria-label="Book cover: The Silent Lattice, handbook for building hybrid clouds">
    <defs>
      <linearGradient id="cloud-tone" x1="0" y1="0" x2="1" y2="1">
        <stop offset="0" stop-color="#1ea3d4"/>
        <stop offset="1" stop-color="#0d6e9b"/>
      </linearGradient>
      <linearGradient id="base-tone" x1="0" y1="1" x2="1" y2="0">
        <stop offset="0" stop-color="var(--sky)"/>
        <stop offset="1" stop-color="var(--sky-deep)"/>
      </linearGradient>
      <clipPath id="title-clip">
        <rect x="0" y="0" width="423" height="558"/>
      </clipPath>
    </defs>

    <rect class="cover-paper" width="423" height="558" fill="var(--paper)"/>

    <g class="author-line">
      <rect x="54" y="35" width="9" height="9" fill="var(--ink)"/>
      <text class="author-name" x="68" y="46">CORWIN HADDLE</text>
      <rect x="232" y="35" width="9" height="9" fill="var(--ink)"/>
      <text class="author-name" x="246" y="46">ROSS PELLEY</text>
    </g>

    <polygon class="band-sun" points="0,333 423,176 423,428 113,558 0,558" fill="var(--sun)"/>
    <polygon class="band-sky" points="113,558 423,428 423,558" fill="url(#base-tone)" role="img" aria-label="Faceted blue low-poly surface"/>
    <polygon class="band-bar" points="0,522 128,475 128,508 0,556" fill="var(--bar)"/>

    <rect class="gear-icons" x="36" y="96" width="26" height="28" rx="6" fill="var(--sky)" role="img" aria-label="Small blue gear icons"/>
    <rect class="hero-cloud" x="58" y="84" width="330" height="152" rx="76" fill="url(#cloud-tone)" role="img" aria-label="Faceted blue cloud with a white upload arrow"/>
    <rect class="device-cloud" x="26" y="252" width="84" height="38" rx="19" fill="var(--sky)" role="img" aria-label="Small blue cloud holding a laptop"/>

    <g class="title-block" clip-path="url(#title-clip)">
      <g transform="translate(48,390) rotate(-20.4)">
        <text class="title-lead" x="0" y="0">THE SILENT</text>
        <text class="title-main" x="-30" y="64" textLength="380" lengthAdjust="spacingAndGlyphs">LATTICE</text>
        <rect class="title-cut" x="-34" y="34" width="390" height="3" fill="var(--sun)"/>
        <text class="tagline" x="44" y="92">HANDBOOK FOR</text>
        <text class="tagline" x="50" y="110">BUILDING HYBRID CLOUDS</text>
      </g>
    </g>
  </svg>
</main>
</body>
</html>
```